Tessel Mobile website

Hello. Pray all is well. Peace be with you.

looking to make a website with pages information from https://velidacel.us. English and Spanish.

the header of tarnwireless.com when in mobile version

clean vector images and layout of quellphone.com

and the clean simple black and white look of pavlitrade.com

please use the attached logo for color guidance

also need the my account section for users to be designed

there should also be a countdown timer for days:hours:seconds on the home page

please do website in figma

```html
<!DOCTYPE html>
<html lang="en">
<head>
<meta charset="utf-8">
<title>Tessel Mobile — Home</title>
<link rel="stylesheet" href="https://fonts.googleapis.com/css2?family=Lexend:wght@400;500;600;700;800&family=Poppins:wght@400;500;600;700&display=swap">
<style>
:root{
  --ink:#0d0d0d;
  --white:#ffffff;
  --soft:#f1f1f1;
  --line:#d6d6d6;
  --muted:#5a5a5a;
  --star:#f4a21d;
  --dark-a:#2a2a2a;
  --dark-b:#050505;
}
*{box-sizing:border-box;margin:0;padding:0}
html,body{width:1200px;height:4481px;overflow:hidden}
body{background:var(--white);color:var(--ink);font-family:"Poppins",sans-serif;position:relative}
.abs{position:absolute}
.ph{border-radius:inherit}

/* header */
.brand{display:flex;flex-direction:column;align-items:center;gap:6px}
.brand-mark{width:56px;height:56px;background:var(--ink)}
.brand-name{font-family:"Poppins",sans-serif;font-weight:600;font-size:22px;color:var(--ink);letter-spacing:-.01em}
.site-header .brand{left:72px;top:14px}
.topbar{right:74px;top:17px;display:flex;gap:12px}
.btn-account{background:var(--ink);color:var(--white);font-size:14px;font-weight:500;padding:0 20px;height:38px;border-radius:20px;display:flex;align-items:center;letter-spacing:.04em}
.lang{border:1px solid var(--line);border-radius:20px;height:38px;width:132px;display:flex;align-items:center;justify-content:space-between;padding:0 16px;font-size:12px}
.nav{left:366px;top:78px;display:flex;gap:32px;font-family:"Lexend",sans-serif;font-size:14px;letter-spacing:.04em;color:#333}
.nav .active{font-weight:700;color:var(--ink)}

/* hero */
.hero{left:75px;top:118px;width:1052px;height:534px;background:var(--soft);border-radius:46px;overflow:hidden}
.hero h1{position:absolute;left:27px;top:44px;font-family:"Lexend",sans-serif;text-transform:uppercase;font-size:46px;line-height:50px;font-weight:500;letter-spacing:.05em;white-space:nowrap}
.hero h1 strong{font-weight:800}
.hero p{position:absolute;left:29px;top:254px;width:480px;font-size:15px;line-height:28px}
.btn-buy{position:absolute;left:29px;top:357px;width:152px;height:58px;border-radius:30px;background:var(--ink);color:var(--white);font-family:"Lexend",sans-serif;font-weight:700;font-size:17px;letter-spacing:.06em;display:flex;align-items:center;justify-content:center}
.countdown{position:absolute;left:43px;top:438px;display:flex;gap:18px}
.count{display:flex;flex-direction:column;align-items:center;gap:12px;width:50px}
.count b{width:50px;height:50px;border-radius:50%;border:2px solid #bcbcbc;background:var(--white);display:flex;align-items:center;justify-content:center;font-family:"Lexend",sans-serif;font-size:17px;font-weight:700}
.count span{font-size:11px;letter-spacing:.04em}
.hero-art{position:absolute;left:525px;top:0;width:527px;height:534px;background:radial-gradient(circle at 60% 45%,#f48c5f 0%,#f7a77e 30%,rgba(241,241,241,0) 70%)}

.quick{top:689px;width:242px;height:143px;border-radius:12px;background:linear-gradient(160deg,var(--dark-a),var(--dark-b));color:var(--white);overflow:hidden}
.quick h3{position:absolute;left:22px;top:20px;font-family:"Lexend",sans-serif;font-weight:700;font-size:20px;letter-spacing:.06em}
.quick .chev{position:absolute;right:20px;top:22px}
.quick .ph{position:absolute;left:50px;top:58px;width:150px;height:85px;border-radius:8px 8px 0 0}

/* perks */
.perks{left:0;top:875px;width:1200px;height:308px;background:var(--soft)}
.perk{position:absolute;top:61px;width:240px;display:flex;flex-direction:column;align-items:center;text-align:center}
.perk .icon{width:74px;height:74px;border-radius:10px;background:var(--white);border:1px solid var(--line);display:flex;align-items:center;justify-content:center}
.perk .icon.dark{background:var(--ink);border-color:var(--ink)}
.perk h4{margin-top:28px;font-family:"Lexend",sans-serif;font-weight:500;font-size:18px;line-height:26px;letter-spacing:.03em}

/* offer cards */
.offer{top:1273px;width:329px;height:440px;border-radius:40px;background:linear-gradient(180deg,var(--dark-a) 0%,#111 60%,var(--dark-b) 100%);color:var(--white);overflow:hidden;text-align:center}
.offer h3{margin:24px 20px 0;font-family:"Lexend",sans-serif;font-weight:500;font-size:18px;line-height:26px;letter-spacing:.03em}
.offer .price{font-size:15px;margin-top:6px}
.offer .note{font-size:10.5px;line-height:20px;margin:8px 22px 0}
.pill{display:inline-flex;align-items:center;justify-content:center;background:var(--white);color:var(--ink);font-size:12px;font-weight:700;letter-spacing:.04em;height:34px;border-radius:18px;padding:0 14px;margin-top:14px}
.offer .ph{position:absolute;left:0;right:0;bottom:0;border-radius:0}

/* steps */
.section-title{font-family:"Lexend",sans-serif;text-transform:uppercase;font-size:30px;font-weight:500;letter-spacing:.04em}
.section-title strong{font-weight:800}
.steps-title{left:0;width:1200px;top:1772px;text-align:center}
.step{top:1849px;width:242px;height:189px;background:var(--white);border-radius:6px;box-shadow:0 4px 14px rgba(0,0,0,.14);overflow:hidden}
.step .num{position:absolute;right:14px;bottom:-14px;font-family:"Lexend",sans-serif;font-weight:800;font-size:110px;color:#ececec;line-height:1}
.step .ico{position:absolute;left:16px;top:26px}
.step h4{position:absolute;left:14px;top:100px;font-family:"Lexend",sans-serif;font-weight:500;font-size:18px;line-height:26px;letter-spacing:.03em;z-index:1}
.step.dark{background:var(--ink);color:var(--white);text-align:center}
.step.dark h4{left:0;right:0;top:54px}
.step.dark .pill{position:absolute;left:30px;right:30px;top:136px;margin:0;font-size:11px}

/* faq */
.faq-band{left:0;top:2122px;width:1200px;height:805px;background:var(--soft)}
.faq-title{left:75px;top:2200px}
.faq{height:50px;width:511px;border:1px solid #b9b9b9;border-radius:26px;background:var(--white);display:flex;align-items:center;justify-content:space-between;padding:0 18px;font-size:14.5px}
.faq b{font-size:22px;font-weight:600}
.btn-outline{width:225px;height:52px;border:1px solid #999;border-radius:28px;display:flex;align-items:center;justify-content:center;font-family:"Lexend",sans-serif;font-weight:700;font-size:12.5px;letter-spacing:.04em;background:transparent}

/* reviews */
.reviews-title{left:0;width:1200px;top:2740px;text-align:center}
.review{top:2811px;width:423px;height:233px;background:var(--white);box-shadow:0 4px 16px rgba(0,0,0,.15);border-radius:4px}
.review .avatar{position:absolute;left:20px;top:28px;width:56px;height:56px;border-radius:50%;background:linear-gradient(135deg,#8a6a5a,#d9c2b0)}
.review h5{position:absolute;left:90px;top:35px;font-family:"Lexend",sans-serif;font-weight:700;font-size:17px;letter-spacing:.04em}
.review .stars{position:absolute;left:90px;top:60px;display:flex;gap:6px}
.review p{position:absolute;left:20px;top:110px;width:370px;font-size:12.5px;line-height:24px}

/* coverage */
.coverage{left:75px;top:3218px;width:1052px;height:306px;background:var(--soft);border-radius:40px}
.coverage .ph{position:absolute;left:26px;top:61px;width:473px;height:214px;border-radius:4px;background:radial-gradient(ellipse at 50% 50%,#b5b5b5 0%,#d4d4d4 55%,var(--soft) 80%)}
.coverage h2{position:absolute;left:541px;top:72px;font-family:"Lexend",sans-serif;text-transform:uppercase;letter-spacing:.04em;font-size:32px;font-weight:500}
.coverage h2 strong{font-weight:800}
.coverage .sub{position:absolute;left:541px;top:120px;font-size:24px;letter-spacing:.02em}
.zip{position:absolute;left:541px;top:177px;width:445px;height:50px;border:1px solid #bbb;border-radius:26px;background:var(--white);display:flex;align-items:center;justify-content:space-between;padding:0 5px 0 20px;font-size:14.5px;color:#444}
.zip b{width:42px;height:42px;border-radius:50%;background:var(--ink);color:var(--white);display:flex;align-items:center;justify-content:center;font-size:12px;font-weight:700}

/* blog */
.blog-title{left:72px;top:3585px}
.post{top:3656px;width:329px}
.post .ph{height:205px;border-radius:8px}
.post time{display:block;margin-top:33px;font-family:"Lexend",sans-serif;font-size:17px;font-weight:500;letter-spacing:.03em}
.post h3{margin-top:6px;font-family:"Lexend",sans-serif;font-size:19px;font-weight:500;line-height:27px;letter-spacing:.04em;text-transform:uppercase;width:310px}
.post a{display:inline-block;margin-top:12px;font-size:12px;font-weight:600;text-decoration:underline;color:var(--ink)}

/* footer */
.site-footer{left:0;top:4141px;width:1200px;height:340px;background:var(--ink);color:var(--white)}
.site-footer .brand{position:absolute;left:96px;top:68px}
.site-footer .brand-mark{background:var(--white);width:68px;height:68px}
.site-footer .brand-name{color:var(--white);font-size:27px;font-weight:500}
.copy{position:absolute;left:60px;top:200px;width:260px;text-align:center;font-size:11.5px;line-height:19px}
.socials{position:absolute;left:103px;top:266px;display:flex;gap:20px}
.socials i{width:20px;height:20px;border-radius:50%;background:#8a8a8a;display:block}
.fcol{position:absolute;top:70px}
.fcol h6{font-family:"Lexend",sans-serif;font-weight:700;font-size:19px;letter-spacing:.06em;margin-bottom:10px}
.fcol a{display:block;color:var(--white);font-size:13.5px;text-decoration:none;line-height:35px}
.fcol h6.gap{margin-top:10px}
</style>
</head>
<body>

<header class="site-header">
  <div class="brand abs"><span class="brand-mark"></span><span class="brand-name">tesselmobile</span></div>
  <div class="topbar abs">
    <span class="btn-account">MY ACCOUNT</span>
    <span class="lang">ENGLISH <span>&#8597;</span></span>
  </div>
  <nav class="nav abs">
    <span class="active">HOME</span><span>BRING YOUR OWN PHONE</span><span>COVERAGE CHECK</span><span>ABOUT US</span><span>SUPPORT</span><span>BLOG</span>
  </nav>
</header>

<section class="hero abs">
  <div class="hero-art" role="img" aria-label="Illustration of a smiling man giving a thumbs up beside a giant smartphone showing the brand"></div>
  <h1>Connect to the<br>future with our 5G<br>networks at<br><strong>Tessel Mobiles</strong></h1>
  <p>Discover our ultra-fast data plans and stylish phones that will make you feel like a star. Ready to conquer your digital world?</p>
  <span class="btn-buy">BUY NOW</span>
  <div class="countdown">
    <div class="count"><b>10</b><span>DAYS</span></div>
    <div class="count"><b>36</b><span>HRS</span></div>
    <div class="count"><b>25</b><span>MINS</span></div>
    <div class="count"><b>15</b><span>SEC</span></div>
  </div>
</section>

<a class="quick abs" style="left:344px">
  <h3>PLANS</h3>
  <svg class="chev" width="14" height="14" viewBox="0 0 14 14" fill="none" stroke="#fff" stroke-width="1.8"><path d="M2 3l4 4-4 4M7 3l4 4-4 4"/></svg>
  <div class="ph" role="img" aria-label="Illustration of colourful SIM cards" style="background:linear-gradient(90deg,#e0413a,#f3c233)"></div>
</a>
<a class="quick abs" style="left:614px">
  <h3>PHONES</h3>
  <svg class="chev" width="14" height="14" viewBox="0 0 14 14" fill="none" stroke="#fff" stroke-width="1.8"><path d="M2 3l4 4-4 4M7 3l4 4-4 4"/></svg>
  <div class="ph" role="img" aria-label="Two purple smartphones showing app icons" style="background:linear-gradient(120deg,#3b1a5e,#8a3cc8)"></div>
</a>

<section class="perks abs">
  <div class="perk" style="left:75px">
    <span class="icon"><svg width="30" height="24" viewBox="0 0 30 24" fill="#222"><path d="M11 2h17v14H11zM2 9l4-5h4v12H2z"/><circle cx="7" cy="19" r="3"/><circle cx="22" cy="19" r="3"/></svg></span>
    <h4>FREE 2-DAY SHIPPING,<br>SERIOUSLY!</h4>
  </div>
  <div class="perk" style="left:344px">
    <span class="icon dark"><svg width="28" height="28" viewBox="0 0 28 28"><circle cx="14" cy="14" r="13" fill="#fff"/><path d="M8 14l4 4 8-8" fill="none" stroke="#000" stroke-width="3"/></svg></span>
    <h4>NO CREDIT CHECK,<br>NO STRESS</h4>
  </div>
  <div class="perk" style="left:616px">
    <span class="icon"><svg width="30" height="24" viewBox="0 0 30 24" fill="none" stroke="#222" stroke-width="3" stroke-linecap="round"><path d="M3 8a17 17 0 0124 0M8 13a10 10 0 0114 0"/><circle cx="15" cy="19" r="2" fill="#222"/></svg></span>
    <h4>5G SPEED AT FULL<br>THROTTLE!</h4>
  </div>
  <div class="perk" style="left:885px">
    <span class="icon"><svg width="20" height="26" viewBox="0 0 20 26" fill="#222"><path d="M0 0h13l7 7v19H0z"/><path d="M4 12h12M4 16h12M4 20h8" stroke="#fff" stroke-width="2"/></svg></span>
    <h4>ZERO ANNUAL<br>CONTRACTS, ZERO<br>HASSLE!</h4>
  </div>
</section>

<article class="offer abs" style="left:75px">
  <h3>BRING YOUR OWN<br>PHONE AND USE IT WITH<br>TESSEL MOBILES</h3>
  <span class="pill">EXPLORE OUR OFFERS</span>
  <div class="ph" role="img" aria-label="White SIM card with a gold chip" style="top:160px;background:linear-gradient(160deg,#111 0%,#e9e9e9 45%,#cfcfcf 100%)"></div>
</article>
<article class="offer abs" style="left:437px">
  <h3>BUY A NEW PHONE<br>CORVEXA 15 PRO</h3>
  <div class="price">$799 / $1000</div>
  <span class="pill" style="width:180px">SEE ALL</span>
  <div class="ph" role="img" aria-label="Purple smartphone front view" style="left:104px;right:104px;top:172px;border-radius:22px 22px 0 0;background:linear-gradient(180deg,#6b2fb3,#2a1250)"></div>
</article>
<article class="offer abs" style="left:798px">
  <h3>DEVICE CHECKER</h3>
  <p class="note">Before you dive into enjoying our plans, make sure your device is compatible with our network.</p>
  <span class="pill" style="width:180px">CHECK YOUR DEVICE</span>
  <div class="ph" role="img" aria-label="Close-up of a purple smartphone home screen" style="left:58px;right:58px;top:172px;border-radius:34px 34px 0 0;background:linear-gradient(180deg,#9a52d8,#4a1a86)"></div>
</article>

<h2 class="section-title steps-title abs">Easy activation <strong>process</strong></h2>
<div class="step abs" style="left:75px">
  <svg class="ico" width="44" height="44" viewBox="0 0 44 44" fill="none" stroke="#333" stroke-width="3"><circle cx="22" cy="22" r="19"/><path d="M3 22h38M22 3c-9 10-9 28 0 38M22 3c9 10 9 28 0 38"/></svg>
  <h4>CHECK<br>COVERAGE IN YOUR<br>AREA</h4><span class="num">1</span>
</div>
<div class="step abs" style="left:344px">
  <svg class="ico" width="44" height="44" viewBox="0 0 44 44" fill="none" stroke="#333" stroke-width="3"><rect x="11" y="2" width="22" height="40" rx="4"/><path d="M19 36h6"/></svg>
  <h4>BRING YOUR<br>PHONE OR GET A<br>NEW ONE</h4><span class="num">2</span>
</div>
<div class="step abs" style="left:616px">
  <svg class="ico" width="48" height="40" viewBox="0 0 48 40" fill="#333"><rect x="0" y="2" width="8" height="7"/><rect x="13" y="3" width="35" height="5"/><rect x="0" y="16" width="8" height="7"/><rect x="13" y="17" width="35" height="5"/><rect x="0" y="30" width="8" height="7"/><rect x="13" y="31" width="35" height="5"/></svg>
  <h4>CHOOSE THE<br>PLAN YOU LIKE<br>BEST</h4><span class="num">3</span>
</div>
<div class="step dark abs" style="left:885px">
  <svg style="position:absolute;left:105px;top:14px" width="32" height="34" viewBox="0 0 32 34" fill="#fff"><path d="M3 10h26l-2 24H5z"/><path d="M10 12V8a6 6 0 0112 0v4" fill="none" stroke="#fff" stroke-width="3"/></svg>
  <h4>PLACE YOUR<br>ORDER &amp; ACTIVATE<br>YOUR PLAN</h4>
  <span class="pill">ACTIVATE YOUR PLAN</span>
</div>

<section class="faq-band abs"></section>
<h2 class="section-title faq-title abs">The answer to <strong>all your questions</strong></h2>
<div class="faq abs" style="left:75px;top:2273px"><span>Duis aute irure dolor in reprehenderit in voluptate?</span><b>+</b></div>
<div class="faq abs" style="left:616px;top:2273px"><span>Duis aute irure dolor in reprehenderit in voluptate?</span><b>+</b></div>
<div class="faq abs" style="left:75px;top:2343px"><span>Velit esse cillum dolore eu fugiat nulla?</span><b>+</b></div>
<div class="faq abs" style="left:616px;top:2343px"><span>Velit esse cillum dolore eu fugiat nulla?</span><b>+</b></div>
<div class="faq abs" style="left:75px;top:2413px"><span>Excepteur sint occaecat cupidatat non proidentsunt?</span><b>+</b></div>
<div class="faq abs" style="left:616px;top:2413px"><span>Excepteur sint occaecat cupidatat non proidentsunt?</span><b>+</b></div>
<div class="faq abs" style="left:75px;top:2482px"><span>Culpa qui officia deserunt mollit?</span><b>+</b></div>
<div class="faq abs" style="left:616px;top:2482px"><span>Culpa qui officia deserunt mollit?</span><b>+</b></div>
<span class="btn-outline abs" style="left:487px;top:2590px">SEE ALL QUESTIONS</span>

<svg width="0" height="0" style="position:absolute"><defs><path id="st" d="M8 0l2.4 5 5.6.6-4.2 3.8 1.2 5.6L8 12.2 3 15l1.2-5.6L0 5.6 5.6 5z"/></defs></svg>

<h2 class="section-title reviews-title abs">Customer <strong>reviews</strong></h2>
<article class="review abs" style="left:165px">
  <div class="avatar" role="img" aria-label="Customer portrait"></div>
  <h5>NAME HEADING</h5>
  <div class="stars"><svg width="100" height="16" viewBox="0 0 100 16" fill="#f4a21d"><use href="#st"/><use href="#st" x="21"/><use href="#st" x="42"/><use href="#st" x="63"/><use href="#st" x="84"/></svg></div>
  <p>“ Duis aute irure dolor in reprehenderit in voluptate velit esse cillum dolore eu fugiat nulla pariaturcepteur sint occaecat cupidatat non proident, sunt in culpa qui officia deserunt mollit anim id est laborum.”</p>
</article>
<article class="review abs" style="left:616px">
  <div class="avatar" role="img" aria-label="Customer portrait" style="background:linear-gradient(135deg,#555,#a9a9a9)"></div>
  <h5>NAME HEADING</h5>
  <div class="stars"><svg width="100" height="16" viewBox="0 0 100 16" fill="#f4a21d"><use href="#st"/><use href="#st" x="21"/><use href="#st" x="42"/><use href="#st" x="63"/><use href="#st" x="84"/></svg></div>
  <p>“ Duis aute irure dolor in reprehenderit in voluptate velit esse cillum dolore eu fugiat nulla pariaturcepteur sint occaecat cupidatat non proident, sunt in culpa qui officia deserunt mollit anim id est laborum.”</p>
</article>
<span class="btn-outline abs" style="left:487px;top:3103px">READ ALL REVIEWS</span>

<section class="coverage abs">
  <div class="ph" role="img" aria-label="Dotted world map"></div>
  <h2>Coverage <strong>checker</strong></h2>
  <p class="sub">Enter your zip code to get started.</p>
  <div class="zip"><span>Check your coverage</span><b>GO</b></div>
</section>

<h2 class="section-title blog-title abs">Recent <strong>blog posts</strong></h2>
<article class="post abs" style="left:75px">
  <div class="ph" role="img" aria-label="Man in an orange shirt smiling at his phone against a yellow wall" style="background:linear-gradient(135deg,#f0b21c,#e86a1c)"></div>
  <time>APRIL 06, 2025</time>
  <h3>Excepteur sint occaecat cupidatat non pr rat ione voluptatem sequi nesciunt.</h3>
  <a>READ MORE</a>
</article>
<article class="post abs" style="left:437px">
  <div class="ph" role="img" aria-label="Couple sitting together looking at a phone" style="background:linear-gradient(135deg,#9aa58a,#d8d0c4)"></div>
  <time>APRIL 06, 2025</time>
  <h3>Excepteur sint occaecat cupidatat non pr rat ione voluptatem sequi nesciunt.</h3>
  <a>READ MORE</a>
</article>
<article class="post abs" style="left:798px">
  <div class="ph" role="img" aria-label="Hands holding a smartphone near a laptop" style="background:linear-gradient(135deg,#6b4a3c,#c9b3a4)"></div>
  <time>APRIL 06, 2025</time>
  <h3>Excepteur sint occaecat cupidatat non pr rat ione voluptatem sequi nesciunt.</h3>
  <a>READ MORE</a>
</article>

<footer class="site-footer abs">
  <div class="brand"><span class="brand-mark"></span><span class="brand-name">tesselmobile</span></div>
  <p class="copy">Copyright © 2025.Company Name<br>All Right Reserved</p>
  <div class="socials"><i></i><i></i><i></i><i></i><i></i></div>
  <div class="fcol" style="left:348px"><h6>TRADE</h6><a>My account</a><a>Planes</a><a>Telephones</a><a>Add data</a></div>
  <div class="fcol" style="left:517px"><h6>FEATURES</h6><a>Bring your phone</a><a>Check your device</a><a>Check your coverage</a></div>
  <div class="fcol" style="left:737px"><h6>ABOUT US</h6><a>Why Tessel Mobile?</a><a>Contact</a><a>Coverage information</a><a>Reviews</a><a>Blog</a></div>
  <div class="fcol" style="left:958px"><h6>SUPPORT</h6><a>Help Center</a><h6 class="gap">LEGAL</h6><a>Terms and conditions</a></div>
</footer>

</body>
</html>
```